Postcard Design

We need a postcard design size DL, front and back in colour, for a Excavation and Earthmoving company specialising in residential jobs including landscaping, drainage, pool excavations and fill ins, footings, trenching, driveways, retaining walls and after build clean ups
using images from out plazafolio page https://www.plazafolio.example/4926038175314807/photos/pb.4926038175314807.-3318640000.2550117792./4718329840636279/?type=3&theater

```html
<!DOCTYPE html>
<html lang="en">
<head>
<meta charset="utf-8">
<title>Digger Dan Earthworks – DL Postcard</title>
<link href="https://fonts.googleapis.com/css2?family=Krona+One&family=Oswald:wght@400;500;600&family=Questrial&display=swap" rel="stylesheet">
<style>
  :root {
    --canvas: #e4e4e4;
    --paper: #ffffff;
    --green: #84c225;
    --grey-text: #5f5f5f;
    --ink: #1e1e1e;
    --photo-soil: #5a4a36;
    --photo-sky: #8fb3cf;
    --photo-grass: #4f7a2a;
  }
  * { box-sizing: border-box; margin: 0; padding: 0; }
  html, body { width: 1200px; height: 1011px; overflow: hidden; }
  body { background: var(--canvas); position: relative; font-family: "Questrial", sans-serif; }

  .card { position: absolute; left: 176px; width: 847px; height: 400px; background: var(--paper); overflow: hidden; }
  .card--front { top: 92px; }
  .card--back { top: 518px; height: 399px; }

  .front-art { position: absolute; inset: 0; }

  .brand { position: absolute; left: 556px; top: 58px; width: 270px; text-align: center;
    font-family: "Krona One", sans-serif; color: var(--green); font-size: 22px; line-height: 32px; }

  .slogan { position: absolute; right: 32px; top: 156px; text-align: right;
    font-family: "Questrial", sans-serif; color: var(--grey-text); font-size: 16px; line-height: 22px;
    -webkit-text-stroke: 0.4px var(--grey-text); }

  .services { position: absolute; left: 0; top: 268px; width: 847px; height: 77px;
    display: flex; align-items: center; justify-content: center; text-align: center;
    font-family: "Krona One", sans-serif; color: #fff; font-size: 14px; line-height: 22px; letter-spacing: 0.3px; }

  .contacts { position: absolute; left: 25px; top: 354px; font-family: "Oswald", sans-serif;
    font-size: 19px; font-weight: 500; color: var(--grey-text); white-space: nowrap; letter-spacing: -0.3px; }
  .contacts .name { color: var(--green); font-weight: 600; }
  .contacts .dot { color: var(--green); margin: 0 5px; }

  .tagline { position: absolute; right: 28px; top: 359px; font-family: "Oswald", sans-serif;
    font-size: 15px; color: var(--green); }

  .machine-band { position: absolute; left: 0; top: 0; width: 847px; height: 109px; background: var(--green);
    display: flex; align-items: center; justify-content: center; text-align: center; padding-bottom: 10px;
    font-family: "Krona One", sans-serif; color: var(--ink); font-size: 13px; line-height: 20px; letter-spacing: 0.4px; }
</style>
</head>
<body>

<section class="card card--front">
  <svg class="front-art" width="847" height="400" viewBox="0 0 847 400">
    <defs>
      <linearGradient id="photoTone" x1="0" y1="0" x2="0" y2="1">
        <stop offset="0" stop-color="var(--photo-sky)"/>
        <stop offset="0.3" stop-color="#6f7a5e"/>
        <stop offset="0.55" stop-color="var(--photo-soil)"/>
        <stop offset="1" stop-color="var(--photo-grass)"/>
      </linearGradient>
      <linearGradient id="bandTone" x1="0" y1="0" x2="1" y2="0">
        <stop offset="0" stop-color="#101a08" stop-opacity="0.85"/>
        <stop offset="0.55" stop-color="#2f4a10" stop-opacity="0.75"/>
        <stop offset="0.8" stop-color="var(--green)"/>
        <stop offset="1" stop-color="var(--green)"/>
      </linearGradient>
      <clipPath id="photoShape">
        <path d="M0 0 H494 C520 60 600 110 630 200 C650 260 660 330 664 345 H0 Z"/>
      </clipPath>
    </defs>
    <rect role="img" aria-label="Photo of a mini excavator digging a backyard site with a worker in hi-vis" x="0" y="0" width="847" height="345" fill="url(#photoTone)" clip-path="url(#photoShape)"/>
    <rect x="0" y="268" width="847" height="77" fill="url(#bandTone)"/>
    <path d="M494 0 C520 60 600 110 630 200 C660 280 668 350 664 400" fill="none" stroke="var(--green)" stroke-width="9"/>
    <path d="M482 0 C488 10 494 18 500 26" fill="none" stroke="#777" stroke-width="7"/>
  </svg>

  <div class="brand">Digger Dan<br>Earthworks</div>

  <p class="slogan">"We can't move heaven,<br>But we can move earth"</p>

  <p class="services">Landscaping, Drainage, Pool Excavations And Fill Ins, Footings,<br>Trenching, Driveways, Retaining Walls And After Build Clean Ups</p>

  <p class="contacts"><span class="name">Callum</span> - 0412-555-019<span class="dot">•</span><span class="name">Marcus</span> - 0413-555-274<span class="dot">•</span>diggerdanearth@mailbox.example</p>

  <p class="tagline">No job too big or small</p>
</section>

<section class="card card--back">
  <p class="machine-band">Extremaly manoiurase machine specialisng in light access jobs<br>excavtor, 700mm wide x 1400mm high, Etc. Through a standar door<br>track loader, 1225mm wide x 1800 high</p>
</section>

</body>
</html>
```